Shop Window Desgin

I have a big glass window (office), 280cm wide by 302cm high and I want designing an advert for our property management business.

Our main colours are in the proeprty management logo attached. I have also uploaded a photo of the shop front (left window), please take into consideration the door.

I want the following text items placed:

PROPERTY MANAGEMENT
HOLIDAY RENTALS
KEYHOLDING
MARKETING & RESERVATIONS
GARDEN & POOL MAINTENACE
CLEANING & LAUNDRY

```html
<!DOCTYPE html>
<html lang="en">
<head>
<meta charset="utf-8">
<title>Northgate Property Management – Shop Window</title>
<link rel="stylesheet" href="https://fonts.googleapis.com/css2?family=Barlow+Condensed:ital,wght@1,700&family=Montserrat:wght@600;900&display=swap">
<style>
  :root {
    --brand-orange: #e8812a;
    --brand-orange-dark: #c96a1c;
    --brand-grey: #6b6b6b;
    --white: #ffffff;
    --backdrop: #2e2e2e;
    --photo-blue: #3d5f8e;
    --photo-light: #b9cbdc;
  }
  * { margin: 0; padding: 0; box-sizing: border-box; }
  html, body {
    width: 1200px; height: 1200px; overflow: hidden;
    background: var(--backdrop);
  }
  .window-advert {
    position: absolute; left: 80px; top: 40px;
    width: 1040px; height: 1120px;
    background: var(--white);
    overflow: hidden;
  }
  .hero-photo {
    position: absolute; left: 0; top: 100px; width: 1040px; height: 540px;
    background:
      radial-gradient(circle at 62% 52%, #3fa9ee 0%, #2e7fc4 12%, transparent 30%),
      radial-gradient(ellipse at 72% 60%, var(--photo-blue) 0%, #4b6a92 35%, transparent 65%),
      linear-gradient(90deg, #8fa6bd 0%, var(--photo-light) 35%, #a9bfd4 70%, #c7d6e3 100%);
  }
  .shapes { position: absolute; inset: 0; width: 1040px; height: 1120px; }
  .brand {
    position: absolute; top: 24px; left: 0; width: 1040px;
    display: flex; justify-content: center; align-items: center; gap: 18px;
  }
  .brand-mark {
    width: 86px; height: 86px; border-radius: 50%;
    background: var(--brand-orange);
  }
  .brand-name {
    font-family: "Montserrat", sans-serif; font-weight: 900;
    font-size: 66px; line-height: 1; color: var(--brand-orange);
    letter-spacing: 0.5px;
  }
  .brand-tagline {
    font-family: "Montserrat", sans-serif; font-weight: 600;
    font-size: 25px; line-height: 1; color: var(--brand-grey);
    margin-top: 8px;
  }
  .service {
    position: absolute; display: flex; align-items: center; gap: 20px;
  }
  .service-icon {
    width: 112px; height: 112px; border-radius: 50%;
    background: var(--brand-orange);
    border: 4px solid var(--white);
    box-shadow: inset 0 0 0 5px var(--brand-orange-dark), 0 2px 4px rgba(0,0,0,0.25);
    display: flex; align-items: center; justify-content: center;
    flex-shrink: 0;
  }
  .service-icon svg { width: 54px; height: 54px; }
  .service-label {
    font-family: "Barlow Condensed", sans-serif; font-style: italic; font-weight: 700;
    font-size: 44px; line-height: 0.95; color: var(--white);
    text-transform: uppercase; letter-spacing: 0.5px;
  }
  .col-left { left: 110px; }
  .col-right { left: 600px; }
  .row-1 { top: 604px; }
  .row-2 { top: 744px; }
  .row-3 { top: 884px; }
  .partner-badge { position: absolute; }
  .badge-association {
    left: 376px; top: 1046px; width: 160px; height: 34px;
    border-radius: 4px; background: #8b3a2a;
  }
  .badge-certificate {
    left: 566px; top: 1024px; width: 78px; height: 78px;
    border-radius: 50%; background: #2a9ad6; border: 4px solid #1b6fa3;
  }
</style>
</head>
<body>
<main class="window-advert">
  <div class="hero-photo" role="img" aria-label="Photo of a businessman in a blue suit holding a glowing blue wireframe house in his open hand"></div>

  <svg class="shapes" viewBox="0 0 1040 1120" aria-hidden="true">
    <path d="M0 0 H1040 V133 Q520 300 0 125 Z" fill="#ffffff"/>
    <path d="M0 125 Q520 300 1040 133" fill="none" stroke="#e8812a" stroke-width="9"/>
    <path d="M0 606 Q520 470 1040 560 V1120 H0 Z" fill="#ffffff"/>
    <path d="M0 620 Q520 490 1040 598 V1120 H0 Z" fill="#e8812a"/>
  </svg>

  <header class="brand">
    <div class="brand-mark"></div>
    <div>
      <div class="brand-name">NORTHGATE</div>
      <div class="brand-tagline">PROPERTY MANAGEMENT</div>
    </div>
  </header>

  <section class="services">
    <div class="service col-left row-1">
      <div class="service-icon">
        <svg viewBox="0 0 54 54" fill="none" stroke="#fff" stroke-width="2.5" stroke-linejoin="round">
          <rect x="16" y="8" width="22" height="28"/><path d="M21 14h4M29 14h4M21 21h4M29 21h4M21 28h4M29 28h4"/>
          <path d="M6 42 q10-6 20 0 h14 q6 0 8-4"/>
        </svg>
      </div>
      <div class="service-label">Property<br>Management</div>
    </div>
    <div class="service col-right row-1">
      <div class="service-icon">
        <svg viewBox="0 0 54 54" fill="none" stroke="#fff" stroke-width="2.5" stroke-linejoin="round">
          <path d="M6 26 L27 8 L48 26"/><path d="M12 22 V46 H42 V22"/><rect x="18" y="30" width="18" height="9"/>
        </svg>
      </div>
      <div class="service-label">Holiday<br>Rentals</div>
    </div>
    <div class="service col-left row-2">
      <div class="service-icon">
        <svg viewBox="0 0 54 54" fill="none" stroke="#fff" stroke-width="2.5" stroke-linecap="round">
          <circle cx="20" cy="38" r="8"/><path d="M25 32 L40 12 M36 17 l5 4 M33 21 l4 3"/>
        </svg>
      </div>
      <div class="service-label">Keyholding</div>
    </div>
    <div class="service col-right row-2">
      <div class="service-icon">
        <svg viewBox="0 0 54 54" fill="none" stroke="#fff" stroke-width="2.5" stroke-linejoin="round" stroke-linecap="round">
          <path d="M8 22 H16 L34 12 V42 L16 32 H8 Z"/><path d="M14 32 l4 12 h5 l-3-12"/><path d="M40 20 l6-4 M41 27 h7 M40 34 l6 4"/>
        </svg>
      </div>
      <div class="service-label">Marketing &amp;<br>Reservations</div>
    </div>
    <div class="service col-left row-3">
      <div class="service-icon">
        <svg viewBox="0 0 54 54" fill="none" stroke="#fff" stroke-width="2.5" stroke-linecap="round">
          <path d="M16 30 V12 a4 4 0 0 1 8 0 M30 30 V12 a4 4 0 0 1 8 0 M16 18 h14 M16 25 h14"/>
          <path d="M8 36 q4-3 8 0 t8 0 t8 0 t8 0 t8 0 M8 43 q4-3 8 0 t8 0 t8 0 t8 0 t8 0"/>
        </svg>
      </div>
      <div class="service-label">Garden &amp; Pool<br>Maintenance</div>
    </div>
    <div class="service col-right row-3">
      <div class="service-icon">
        <svg viewBox="0 0 54 54" fill="none" stroke="#fff" stroke-width="2.5">
          <rect x="11" y="7" width="32" height="40" rx="3"/><path d="M11 15 H43"/><circle cx="27" cy="31" r="9"/><circle cx="35" cy="11" r="1.5"/>
        </svg>
      </div>
      <div class="service-label">Cleaning &amp;<br>Laundry</div>
    </div>
  </section>

  <footer class="partners">
    <div class="partner-badge badge-association"></div>
    <div class="partner-badge badge-certificate"></div>
  </footer>
</main>
</body>
</html>
```